Lumo4Kart - a fintech company - business card

We need a business card design for our Payments Technology company in Sydney, Australia. We provide business with payment solutions expanding across EFTPOS machines, online payment gateways and mobile payment solutions. We would like to see designs that are clean, classy and professional.
Target Market(s)
Business professionals, executives, c-suite
Industry/Entity Type
Fintech
Contact Information for Business Card
Will be on 400gsm. Logo will most likely be spot gloss unless designer recommends otherwise.
Font styles to use
Sans Serif
Requirements
Must have
- We need our website (lumo4kart.com.au), email (contact@lumo4kart.com.au), mobile (0432 587 904) and direct phone number (02 6815 3927) to feature on the card along with our logo (attached) and the words "EFTPOS | ONLINE | MOBILE"
- Font = Roboto

```html
<!DOCTYPE html>
<html lang="en">
<head>
<meta charset="utf-8">
<title>Lumo4Kart — Business Card</title>
<link href="https://fonts.googleapis.com/css2?family=Roboto:wght@300;400;700&display=swap" rel="stylesheet">
<style>
  :root {
    --stage: #d5d5d5;
    --brand-blue: #215e92;
    --brand-blue-soft: #3b75a6;
    --ink-grey: #5f6164;
    --text-grey: #6d6f72;
    --paper: #ffffff;
    --wash: #dfe6ef;
  }
  * { box-sizing: border-box; margin: 0; padding: 0; }
  html, body {
    width: 1200px; height: 900px; overflow: hidden;
    background: var(--stage);
    font-family: "Roboto", Arial, sans-serif;
  }
  .stage {
    position: relative; width: 1200px; height: 900px;
    display: flex; align-items: center; justify-content: center; gap: 40px;
  }
  .card {
    position: relative; width: 520px; height: 318px; overflow: hidden;
    box-shadow: 0 2px 6px rgba(0,0,0,.18);
  }
  /* Back */
  .card--back {
    background: var(--brand-blue);
    display: flex; align-items: center; justify-content: center;
  }
  .card--back .wordmark {
    font-weight: 700; font-size: 40px; letter-spacing: .5px;
    color: var(--brand-blue-soft);
  }
  /* Front */
  .card--front { background: var(--paper); }
  .decor-circle {
    position: absolute; right: -70px; top: 38px;
    width: 300px; height: 300px; border-radius: 50%;
    background: var(--wash);
  }
  .identity {
    position: absolute; left: 38px; top: 84px;
    display: flex; align-items: center; gap: 10px;
  }
  .identity .mark-dot {
    width: 22px; height: 22px; border-radius: 50%;
    background: var(--brand-blue);
  }
  .identity .wordmark {
    font-weight: 700; font-size: 32px; color: var(--ink-grey);
  }
  .person {
    position: absolute; right: 30px; top: 26px; text-align: right;
  }
  .person .name {
    font-weight: 700; font-size: 17px; color: var(--brand-blue);
  }
  .person .role {
    font-weight: 400; font-size: 12px; color: var(--text-grey); margin-top: 2px;
  }
  .services {
    position: absolute; right: 26px; bottom: 24px;
    font-weight: 300; font-size: 12px; color: var(--text-grey); letter-spacing: .3px;
  }
  .services .sep { color: var(--brand-blue); font-weight: 400; padding: 0 3px; }
  .contacts {
    position: absolute; left: 38px; bottom: 22px;
    list-style: none;
  }
  .contacts li {
    display: flex; align-items: center; gap: 7px;
    font-weight: 300; font-size: 12.5px; line-height: 17px; color: var(--text-grey);
  }
  .contacts svg { width: 11px; height: 11px; flex: none; }
</style>
</head>
<body>
<main class="stage">
  <section class="card card--back" aria-label="Card back">
    <span class="wordmark">Lumo4Kart</span>
  </section>

  <section class="card card--front" aria-label="Card front">
    <div class="decor-circle" aria-hidden="true"></div>

    <div class="identity">
      <span class="mark-dot" aria-hidden="true"></span>
      <span class="wordmark">Lumo4Kart</span>
    </div>

    <div class="person">
      <div class="name">Daniel Whitford</div>
      <div class="role">President</div>
    </div>

    <ul class="contacts">
      <li>
        <svg viewBox="0 0 12 12" aria-hidden="true"><rect x="3" y="0.8" width="6" height="10.4" rx="1" fill="none" stroke="var(--brand-blue)" stroke-width="1.2"/></svg>
        0432 587 904
      </li>
      <li>
        <svg viewBox="0 0 12 12" aria-hidden="true"><path d="M2.5 1 L4.6 1 L5.3 3.6 L4 4.6 Q5 7 7.4 8 L8.4 6.7 L11 7.4 L11 9.5 Q10.5 11 9 11 Q1 10 1 3 Q1 1.5 2.5 1Z" fill="var(--brand-blue)"/></svg>
        02 6815 3927
      </li>
      <li>
        <svg viewBox="0 0 12 12" aria-hidden="true"><rect x="0.8" y="2.2" width="10.4" height="7.6" fill="none" stroke="var(--brand-blue)" stroke-width="1.2"/><path d="M0.8 2.2 L6 6.6 L11.2 2.2" fill="none" stroke="var(--brand-blue)" stroke-width="1.2"/></svg>
        contact@lumo4kart.com.au
      </li>
      <li>
        <svg viewBox="0 0 12 12" aria-hidden="true"><g fill="none" stroke="var(--brand-blue)" stroke-width="1"><circle cx="6" cy="6" r="5"/><ellipse cx="6" cy="6" rx="2.2" ry="5"/><path d="M1 6 H11 M2 3.3 H10 M2 8.7 H10"/></g></svg>
        lumo4kart.com.au
      </li>
    </ul>

    <div class="services">EFTPOS<span class="sep">|</span>ONLINE<span class="sep">|</span>MOBILE</div>
  </section>
</main>
</body>
</html>
```